Website design for a Recruitment Agency in the Pacific Islands

Website for jobseekers to search for work, employers to list vacancies and also for workers to upload their resumes for possible job prospects.

The website will be called ' Korowai Staffing' and this needs to reflect the Pacific Islanders searching for jobs or working in the fields.
Must be connected to a database that collects details for workers which can be downloaded onto an excel spreadsheet for quick reviews offline
The website must also have an app for ios and android so this can be easily downloaded for individuals who want to do quick job searches without going onto the website.

The main objective of this website is to list job opportunities in all Pacific Island Countries or even overseas which Pacific Islanders can apply.

The theme of fishing means ' there is alot of fish in the sea ' = lots of workers in the Pacific Ocean.

Target Market(s)

Agriculture, Fisheries, constructions and mining

Industry/Entity Type

Agriculture, Constructions and Fisheries

Font styles to use
Other font styles liked:
• Muli

Colors
E54698
E96AAD
F1A4CE
F9D9EA
FCEFF6

Requirements
Must have
• Must have an App, adroid and ios
Nice to have
• - pictures of Pacific Islanders , pictures of Pacific Islanders at work in mines, in fisheries and in agricultures

```html
<!DOCTYPE html>
<html lang="en">
<head>
<meta charset="utf-8">
<title>Korowai Staffing — Find the perfect job for you</title>
<link rel="stylesheet" href="https://fonts.googleapis.com/css2?family=Mulish:wght@400;500;600;700;800&display=swap">
<style>
:root{
  --pink:#E6007E;
  --pink-2:#E96AAD;
  --pink-3:#F1A4CE;
  --pink-4:#F9D9EA;
  --pink-5:#FCEFF6;
  --ink:#111111;
  --muted:#666666;
  --line:#d9d9d9;
  --white:#ffffff;
  --black:#000000;
}
*{box-sizing:border-box;margin:0;padding:0}
html,body{width:1200px;height:4412px;overflow:hidden}
body{font-family:"Mulish",Arial,sans-serif;color:var(--ink);background:var(--white);position:relative}
.abs{position:absolute}
a{color:inherit;text-decoration:none}

/* header */
.site-header{position:absolute;left:0;top:0;width:1200px;height:106px;background:var(--white);box-shadow:0 4px 14px rgba(0,0,0,.05);z-index:2}
.brand{position:absolute;left:86px;top:38px;font-size:23px;font-weight:500;letter-spacing:-.3px;color:var(--ink);white-space:nowrap}
.nav{position:absolute;left:310px;top:44px;display:flex;gap:28px;font-size:12.5px;font-weight:500;white-space:nowrap}
.nav a.active{color:var(--pink)}
.upload-btn{position:absolute;left:1007px;top:31px;width:106px;height:44px;border:1.5px solid var(--ink);border-radius:22px;display:flex;align-items:center;justify-content:center;gap:8px;font-size:13px;font-weight:600}

/* hero */
.hero-title{left:84px;top:206px;font-size:58px;font-weight:700;line-height:70px;letter-spacing:-.5px}
.hero-sub{left:86px;top:362px;font-size:15px}
.search-bar{left:86px;top:411px;width:458px;height:82px;background:var(--white);border-radius:41px;box-shadow:0 4px 18px rgba(0,0,0,.12)}
.search-bar .field{position:absolute;top:30px;font-size:14px}
.search-bar .divider{position:absolute;left:128px;top:24px;width:1px;height:34px;background:var(--line)}
.btn{display:flex;align-items:center;justify-content:center;background:var(--pink);color:var(--white);font-weight:600;border-radius:26px}
.search-bar .btn{position:absolute;left:327px;top:16px;width:116px;height:50px;font-size:15px}
.popular-title{left:84px;top:532px;font-size:20px;font-weight:700}
.tag{position:absolute;font-size:15px;color:var(--pink);height:38px;display:flex;align-items:center;padding:0 28px;border-radius:19px}
.tag.raised{background:var(--white);box-shadow:0 2px 10px rgba(0,0,0,.1)}
.hero-media{left:610px;top:106px}

/* sections */
.section-title{position:absolute;left:0;width:1200px;text-align:center;font-size:40px;font-weight:700}
.section-sub{position:absolute;left:0;width:1200px;text-align:center;font-size:13px;color:var(--muted)}
.cat-card{position:absolute;top:974px;width:237px;height:288px;border-radius:36px;background:var(--pink-5);text-align:center}
.cat-card svg{position:absolute;left:96px;top:60px}
.cat-card .name{position:absolute;top:166px;width:100%;font-size:19px;font-weight:700}
.cat-card .count{position:absolute;top:233px;width:100%;font-size:13px}
.cat-card.active{background:var(--pink);color:var(--white)}
.pill-btn{position:absolute;height:50px;font-size:15px;border-radius:25px}

.jobs-band{left:0;top:1462px;width:1200px;height:1157px;background:var(--pink-5)}
.job-card{position:absolute;left:86px;width:1028px;height:215px;background:var(--white);border-radius:36px;box-shadow:0 4px 16px rgba(230,0,126,.08)}
.job-card .avatar{position:absolute;left:44px;top:34px;width:64px;height:64px;border-radius:14px;background:var(--black)}
.job-card .role{position:absolute;left:156px;top:32px;font-size:19px;font-weight:700}
.job-card .meta{position:absolute;left:156px;top:72px;display:flex;align-items:center;gap:8px;font-size:13px}
.job-card .meta b{font-weight:700;margin-right:14px}
.job-card .posted{position:absolute;left:44px;top:146px;font-size:12px;line-height:19px;color:var(--muted)}
.job-card .posted b{color:var(--ink)}
.job-card .btn{position:absolute;left:868px;top:128px;width:116px;height:52px;font-size:15px}

/* about */
.about-back{left:130px;top:2773px;width:351px;height:428px;background:var(--pink);border-radius:38px}
.about-photo{left:86px;top:2731px;width:352px;height:428px;border-radius:38px;background:linear-gradient(160deg,#6f7a5c 0%,#8c8170 45%,#c4b8a4 100%)}
.about-title{left:572px;top:2806px;font-size:40px;font-weight:700;white-space:nowrap}
.about-copy{left:572px;top:2878px;width:540px;font-size:13px;line-height:21px;color:var(--muted)}
.about-copy p+p{margin-top:10px}
.outline-btn{position:absolute;left:572px;top:3077px;width:123px;height:44px;border:1.5px solid var(--ink);border-radius:22px;display:flex;align-items:center;justify-content:center;font-size:13px;font-weight:600}
.about-ring{left:796px;top:2708px;width:190px;height:190px;border:1px solid var(--pink-4);border-radius:50%}

/* contact */
.contact-card{left:86px;top:3313px;width:1028px;height:530px;background:var(--white);border-radius:40px;box-shadow:0 4px 20px rgba(0,0,0,.08)}
.contact-panel{left:96px;top:3321px;width:400px;height:509px;background:var(--pink);border-radius:36px;color:var(--white)}
.contact-panel h2{position:absolute;left:48px;top:84px;font-size:40px;font-weight:700}
.contact-item{position:absolute;left:48px;display:flex;align-items:center;gap:18px;font-size:15px;font-weight:700;line-height:19px}
.contact-item .ico{width:44px;height:44px;border-radius:50%;background:var(--white);display:flex;align-items:center;justify-content:center;flex:none}
.form-title{left:556px;top:3370px;font-size:40px;font-weight:600}
.field-label{position:absolute;font-size:13px;font-weight:700}
.field-line{position:absolute;height:1px;background:var(--line)}
.placeholder{position:absolute;font-size:11px;color:#9a9a9a}
.submit{position:absolute;left:923px;top:3726px;width:124px;height:46px;font-size:15px}

/* footer */
.site-footer{left:0;top:3951px;width:1200px;height:461px;background:var(--black);color:var(--white)}
.site-footer .brand{left:86px;top:64px;color:var(--white);font-size:26px}
.footer-about{position:absolute;left:86px;top:156px;width:350px;font-size:13px;line-height:21px}
.footer-col{position:absolute;top:65px}
.footer-col h3{font-size:16px;font-weight:700}
.footer-col .bar{width:44px;height:3px;background:var(--pink);margin-top:14px;margin-bottom:22px}
.footer-col li{list-style:none;font-size:11.5px;height:42px;display:flex;align-items:center;gap:12px}
.footer-col li::before{content:"»";font-size:12px}
.footer-contact li::before{content:none}
.footer-contact li{align-items:flex-start;height:auto;margin-bottom:22px;line-height:14px;width:240px}
.footer-contact li svg{flex:none;margin-top:1px}
.footer-rule{position:absolute;left:86px;top:391px;width:1028px;height:1px;background:#555}
.copyright{position:absolute;left:0;top:383px;width:1200px;text-align:center;font-size:13px;font-weight:700}
.copyright span{background:var(--black);padding:0 12px}
</style>
</head>
<body>

<header class="site-header">
  <div class="brand">Korowai Staffing</div>
  <nav class="nav">
    <a class="active">Home</a><a>About Us</a><a>Services We Offer Assistance In</a><a>Job Seeker Portal</a><a>Training</a><a>Info</a><a>Contact Us</a>
  </nav>
  <a class="upload-btn">Upload
    <svg width="14" height="14" viewBox="0 0 14 14" fill="none" stroke="#111" stroke-width="1.5"><path d="M7 10V2M4 5l3-3 3 3M2 9v3h10V9"/></svg>
  </a>
</header>

<!-- hero -->
<h1 class="abs hero-title">Find the perfect<br>job for you</h1>
<p class="abs hero-sub">Search your career opportunity through 12,800 jobs</p>
<div class="abs search-bar">
  <span class="field" style="left:37px">Job Title</span>
  <span class="divider"></span>
  <span class="field" style="left:148px;display:flex;align-items:center;gap:6px">
    <svg width="13" height="13" viewBox="0 0 14 14" fill="none" stroke="#111" stroke-width="1.2"><circle cx="7" cy="7" r="6"/><path d="M1 7h12M7 1c2 2 2 10 0 12M7 1c-2 2-2 10 0 12"/></svg>
    All Locations
    <svg width="10" height="10" viewBox="0 0 10 10" fill="none" stroke="#111" stroke-width="1.3" style="margin-left:30px"><path d="M2 4l3 3 3-3"/></svg>
  </span>
  <a class="btn">Find Jobs</a>
</div>
<h2 class="abs popular-title">Popular Searches</h2>
<a class="tag raised" style="left:84px;top:579px">Agriculture</a>
<a class="tag" style="left:228px;top:579px">Fisheries</a>
<a class="tag" style="left:80px;top:628px">Constructions &amp; mining</a>

<svg class="abs hero-media" width="590" height="670" viewBox="0 0 590 670" role="img" aria-label="Photo of a Pacific Islander site worker in hard hat and hi-vis vest reading plans beside a mining truck">
  <defs>
    <linearGradient id="heroTone" x1="0" y1="0" x2="1" y2="1">
      <stop offset="0" stop-color="#9a948a"/>
      <stop offset="0.5" stop-color="#7d756d"/>
      <stop offset="1" stop-color="#c9bfb1"/>
    </linearGradient>
  </defs>
  <path d="M178 0H590V640C560 665 530 668 505 655L38 430C8 415 -4 385 10 355Z" fill="url(#heroTone)"/>
</svg>

<!-- categories -->
<h2 class="section-title" style="top:868px">Search by Category</h2>
<p class="section-sub" style="top:929px">Search your career opportunity with our categories</p>

<div class="cat-card" style="left:86px">
  <svg width="46" height="46" viewBox="0 0 46 46" fill="none" stroke="#111" stroke-width="1.6"><circle cx="20" cy="8" r="4"/><path d="M20 12v14M12 18h16M14 40l6-14 6 14M32 6v34M28 10l4-4 4 4M6 40h34"/></svg>
  <div class="name">Agriculture</div><div class="count">1 open position</div>
</div>
<div class="cat-card active" style="left:349px">
  <svg width="46" height="46" viewBox="0 0 46 46" fill="none" stroke="#fff" stroke-width="1.6"><path d="M23 4v6M23 10c-6 6-6 14 0 20 6-6 6-14 0-20zM23 30v8c0 4-6 4-6 0"/><circle cx="23" cy="20" r="2"/></svg>
  <div class="name">Fisheries</div><div class="count">1 open position</div>
</div>
<div class="cat-card" style="left:613px">
  <svg width="46" height="46" viewBox="0 0 46 46" fill="none" stroke="#111" stroke-width="1.6"><path d="M6 40h34M10 40V8h26M10 14h26M36 8v10M33 18h6v6h-6zM14 22h10v18H14zM14 28h10M14 34h10M19 22v18"/></svg>
  <div class="name">Constructions</div><div class="count">1 open position</div>
</div>
<div class="cat-card" style="left:877px">
  <svg width="46" height="46" viewBox="0 0 46 46" fill="none" stroke="#111" stroke-width="1.6"><path d="M8 10c8-6 18-6 26 0M21 8l-8 16M6 40l14-14 8 6 12-14v22zM28 34l2 2M34 30l2 2"/></svg>
  <div class="name">Mining</div><div class="count">1 open position</div>
</div>
<a class="btn pill-btn" style="left:517px;top:1303px;width:163px">All Category&nbsp;›</a>

<!-- featured jobs -->
<div class="abs jobs-band"></div>
<h2 class="section-title" style="top:1563px">Featured Job-seeker Portal</h2>
<p class="section-sub" style="top:1623px">Search your career opportunity through 12,800 jobs</p>

<article class="job-card" style="top:1691px">
  <div class="avatar"></div>
  <h3 class="role">Agriculture Dept.</h3>
  <div class="meta"><svg width="24" height="24" viewBox="0 0 24 24" fill="none" stroke="#111" stroke-width="1.2"><circle cx="12" cy="12" r="10"/><path d="M2 12h20M12 2c4 4 4 16 0 20M12 2c-4 4-4 16 0 20"/></svg><b>Papua New Guinea</b>Full Time</div>
  <p class="posted">June 8, 2022 by<br><b>Korowai Staffing</b></p>
  <a class="btn">Apply</a>
</article>
<article class="job-card" style="top:1945px">
  <div class="avatar"></div>
  <h3 class="role">Fisheries Dept.</h3>
  <div class="meta"><svg width="24" height="24" viewBox="0 0 24 24" fill="none" stroke="#111" stroke-width="1.2"><circle cx="12" cy="12" r="10"/><path d="M2 12h20M12 2c4 4 4 16 0 20M12 2c-4 4-4 16 0 20"/></svg><b>Australia</b>Internship</div>
  <p class="posted">June 8, 2022 by<br><b>Korowai Staffing</b></p>
  <a class="btn">Apply</a>
</article>
<article class="job-card" style="top:2202px">
  <div class="avatar"></div>
  <h3 class="role">Constructions &amp; mining</h3>
  <div class="meta"><svg width="24" height="24" viewBox="0 0 24 24" fill="none" stroke="#111" stroke-width="1.2"><circle cx="12" cy="12" r="10"/><path d="M2 12h20M12 2c4 4 4 16 0 20M12 2c-4 4-4 16 0 20"/></svg><b>Papua New Guinea</b>Part Time</div>
  <p class="posted">June 8, 2022 by<br><b>Korowai Staffing</b></p>
  <a class="btn">Apply</a>
</article>
<a class="btn pill-btn" style="left:518px;top:2460px;width:162px">All Job Offer&nbsp;›</a>

<!-- about -->
<div class="abs about-back"></div>
<div class="abs about-photo" role="img" aria-label="Photo of a young Pacific Islander worker sitting on timber logs writing in a notebook"></div>
<div class="abs about-ring"></div>
<h2 class="abs about-title">About Korowai Staffing</h2>
<div class="abs about-copy">
  <p>Lorem ipsum dolor sit amet, consectetur adipiscing elit. Praesent ut vehicula lectus. Integer suscipit erat in ligula molestie finibus. Proin ornare ipsum eget risus facilisis volutpat. Nunc tincidunt enim a sapien porttitor, non elementum metus placerat. Curabitur tristique metus at bibendum viverra. Cras hendrerit pellentesque nunc, a cursus leo aliquet sit ame</p>
  <p>Lorem ipsum dolor sit amet, consectetur adipiscing elit. Praesent ut vehicula lectus. Integer suscipit erat in ligula molestie finibus. Proin ornare ipsum eget risus facilisis volutpat.</p>
</div>
<a class="outline-btn">Get Started</a>

<!-- contact -->
<div class="abs contact-card"></div>
<div class="abs contact-panel">
  <h2>Contact Us</h2>
  <div class="contact-item" style="top:182px"><span class="ico"><svg width="20" height="20" viewBox="0 0 24 24" fill="#E6007E"><path d="M6.6 10.8a15 15 0 006.6 6.6l2.2-2.2c.3-.3.7-.4 1-.2 1.1.4 2.3.6 3.6.6.6 0 1 .4 1 1V20c0 .6-.4 1-1 1A17 17 0 013 4c0-.6.4-1 1-1h3.5c.6 0 1 .4 1 1 0 1.3.2 2.5.6 3.6.1.3 0 .7-.2 1z"/></svg></span>Call: 0400 512 078<br>(Australia)</div>
  <div class="contact-item" style="top:256px"><span class="ico"><svg width="20" height="20" viewBox="0 0 24 24" fill="#E6007E"><path d="M6.6 10.8a15 15 0 006.6 6.6l2.2-2.2c.3-.3.7-.4 1-.2 1.1.4 2.3.6 3.6.6.6 0 1 .4 1 1V20c0 .6-.4 1-1 1A17 17 0 013 4c0-.6.4-1 1-1h3.5c.6 0 1 .4 1 1 0 1.3.2 2.5.6 3.6.1.3 0 .7-.2 1z"/></svg></span>Call: 0400 512 078<br>(Papua New Guinea)</div>
  <div class="contact-item" style="top:330px"><span class="ico"><svg width="20" height="16" viewBox="0 0 20 16" fill="none" stroke="#E6007E" stroke-width="1.8"><rect x="1" y="1" width="18" height="14" rx="2"/><path d="M1 2l9 7 9-7"/></svg></span>Email:<br>hello@korowaistaffing.example</div>
  <div class="contact-item" style="top:404px"><span class="ico"><svg width="16" height="20" viewBox="0 0 16 20" fill="#E6007E"><path d="M8 0a8 8 0 00-8 8c0 6 8 12 8 12s8-6 8-12a8 8 0 00-8-8zm0 11a3 3 0 110-6 3 3 0 010 6z"/></svg></span>Location: Papua New<br>Guinea &amp; Australia</div>
</div>
<h2 class="abs form-title">Get in Touch</h2>
<span class="field-label" style="left:556px;top:3446px">First Name</span>
<span class="abs" style="left:557px;top:3470px;width:1px;height:18px;background:#111"></span>
<span class="field-line" style="left:556px;top:3497px;width:236px"></span>
<span class="field-label" style="left:810px;top:3446px">Last Name</span>
<span class="placeholder" style="left:810px;top:3474px">Jhon Doe</span>
<span class="field-line" style="left:810px;top:3497px;width:236px"></span>
<span class="field-label" style="left:556px;top:3532px">Email</span>
<span class="placeholder" style="left:556px;top:3561px">info@example.com</span>
<span class="field-line" style="left:556px;top:3583px;width:236px"></span>
<span class="field-label" style="left:810px;top:3532px">Phone</span>
<span class="placeholder" style="left:810px;top:3561px">+01 234 567 89</span>
<span class="field-line" style="left:810px;top:3583px;width:236px"></span>
<span class="field-label" style="left:556px;top:3617px">Your Message</span>
<span class="placeholder" style="left:556px;top:3646px">Your message here</span>
<span class="field-line" style="left:556px;top:3702px;width:490px"></span>
<a class="btn submit">Submit</a>

<!-- footer -->
<footer class="abs site-footer">
  <div class="brand">Korowai Staffing</div>
  <p class="footer-about">Praesent eu magna ultricies, aliquet eros a, dignissim ligula. Fusce bibendum sed dui sed ultrices. Phasellus sapien tortor, accumsan quis odio sit amet, aliquet auctor mi. Aliquam vulputate tortor ex, laoreet sodales libero tempus quis. Integer convallis porttitor venenatis.</p>
  <div class="footer-col" style="left:496px">
    <h3>Quick Links</h3><div class="bar"></div>
    <ul><li>Home</li><li>About Us</li><li>Services</li><li>Job Seeker portal</li><li>Training</li></ul>
  </div>
  <div class="footer-col" style="left:678px;top:62px">
    <h3>Other Links</h3><div class="bar"></div>
    <ul><li>Our Team</li><li>Gallery</li><li>FAQ</li><li>Reviews</li><li>Contact</li></ul>
  </div>
  <div class="footer-col footer-contact" style="left:863px;top:62px">
    <h3>Contact</h3><div class="bar"></div>
    <ul>
      <li><svg width="12" height="15" viewBox="0 0 16 20" fill="#fff"><path d="M8 0a8 8 0 00-8 8c0 6 8 12 8 12s8-6 8-12a8 8 0 00-8-8zm0 11a3 3 0 110-6 3 3 0 010 6z"/></svg><span><b>Location:</b> Papua New Guinea &amp; Australia</span></li>
      <li><svg width="13" height="13" viewBox="0 0 24 24" fill="#fff"><path d="M6.6 10.8a15 15 0 006.6 6.6l2.2-2.2c.3-.3.7-.4 1-.2 1.1.4 2.3.6 3.6.6.6 0 1 .4 1 1V20c0 .6-.4 1-1 1A17 17 0 013 4c0-.6.4-1 1-1h3.5c.6 0 1 .4 1 1 0 1.3.2 2.5.6 3.6.1.3 0 .7-.2 1z"/></svg><span><b>Call:</b> 0400 512 078 (Papua New Guinea)</span></li>
      <li><svg width="13" height="13" viewBox="0 0 24 24" fill="#fff"><path d="M6.6 10.8a15 15 0 006.6 6.6l2.2-2.2c.3-.3.7-.4 1-.2 1.1.4 2.3.6 3.6.6.6 0 1 .4 1 1V20c0 .6-.4 1-1 1A17 17 0 013 4c0-.6.4-1 1-1h3.5c.6 0 1 .4 1 1 0 1.3.2 2.5.6 3.6.1.3 0 .7-.2 1z"/></svg><span><b>Call:</b> 0400 512 078 (Australia)</span></li>
      <li><svg width="13" height="11" viewBox="0 0 20 16" fill="#fff"><path d="M0 2a2 2 0 012-2h16a2 2 0 012 2v.5l-10 7-10-7zM0 4.5l10 7 10-7V14a2 2 0 01-2 2H2a2 2 0 01-2-2z"/></svg><span><b>Email:</b> hello@korowaistaffing.example</span></li>
    </ul>
  </div>
  <div class="footer-rule"></div>
  <p class="copyright"><span>Copyright © 2022. All right reserved.</span></p>
</footer>

</body>
</html>
```